BrambleWare business card

Looking for business card design that supports our company/software values. We have 2 logo designs at the moment but open to change if you think you can enhance the brand. Check out website www.brambleware.com.au.

Target Market(s)

Education

Contact Information for Business Card

Name, title, mobile, email and website

Font styles to use
Sans Serif

Colors

Designer to choose colors to be used in the design.

Requirements
Must have
• BrambleWare logo with tree and tagline on rear side with dark grey background colour

```html
<!DOCTYPE html>
<html lang="en">
<head>
<meta charset="utf-8">
<title>BrambleWare business card</title>
<link href="https://fonts.googleapis.com/css2?family=Open+Sans:wght@300;400;600&display=swap" rel="stylesheet">
<style>
  :root {
    --backdrop: #eceeee;
    --card-white: #f7f8f8;
    --charcoal: #4a4c4a;
    --ink: #3a3b3a;
    --leaf-green: #3f7f2e;
    --text-light: #e9ecea;
    --text-muted: #c9cdca;
    --rule-light: #9a9d9a;
  }
  * { box-sizing: border-box; margin: 0; padding: 0; }
  html, body {
    width: 1200px; height: 1000px; overflow: hidden;
    background: var(--backdrop);
    font-family: "Open Sans", "Segoe UI", sans-serif;
  }
  .sheet {
    width: 1200px; height: 1000px;
    display: flex; flex-direction: column; align-items: center;
    justify-content: center; gap: 26px;
  }
  .card {
    position: relative;
    width: 800px; height: 457px;
    background: var(--card-white);
    overflow: hidden;
    box-shadow: 0 2px 10px rgba(0,0,0,0.08);
  }
  .card-bg { position: absolute; inset: 0; width: 100%; height: 100%; }

  /* Contact side */
  .contact-block {
    position: absolute; left: 56px; top: 54px;
    color: var(--text-light);
  }
  .person-name {
    font-size: 34px; font-weight: 400; letter-spacing: 1px;
    text-transform: uppercase;
  }
  .person-title {
    font-size: 15px; font-weight: 300; color: var(--text-muted);
    margin-top: 2px;
  }
  .office-line {
    font-size: 15px; font-weight: 300; color: var(--text-muted);
    margin-top: 44px; line-height: 1.35;
  }
  .contact-list { list-style: none; margin-top: 14px; }
  .contact-list li {
    display: flex; align-items: center; gap: 10px;
    font-size: 16px; font-weight: 300; line-height: 1.55;
  }
  .contact-list svg { width: 13px; height: 13px; fill: var(--text-light); flex: none; }

  .brand-lockup {
    position: absolute; display: flex; align-items: center;
  }
  .brand-mark { border-radius: 50%; flex: none; }
  .brand-name { font-weight: 400; }

  .contact-side .brand-lockup { right: 70px; bottom: 110px; gap: 16px; }
  .contact-side .brand-mark { width: 38px; height: 38px; background: var(--charcoal); }
  .contact-side .brand-name { font-size: 40px; color: var(--ink); }

  /* Logo side — dark grey rear */
  .logo-side { background: var(--charcoal); }
  .logo-side .logo-center {
    position: absolute; left: 50%; top: 50%;
    transform: translate(-50%, -50%);
    display: flex; align-items: center; gap: 24px;
  }
  .logo-side .brand-mark { width: 60px; height: 60px; background: var(--text-light); }
  .logo-side .brand-name { font-size: 62px; line-height: 1; color: var(--text-light); }
  .brand-rule { height: 1px; background: var(--rule-light); margin: 10px 0 6px; }
  .tagline { font-size: 22px; color: var(--text-muted); font-weight: 300; letter-spacing: 0.5px; }
</style>
</head>
<body>
<main class="sheet">

  <section class="card contact-side" aria-label="Card front with contact details">
    <svg class="card-bg" viewBox="0 0 800 457" preserveAspectRatio="none" aria-hidden="true">
      <path d="M0,0 H555 C430,120 330,280 318,457 H0 Z" fill="var(--leaf-green)"/>
      <path d="M0,0 H520 C400,125 305,285 296,457 H0 Z" fill="var(--charcoal)"/>
    </svg>

    <div class="contact-block">
      <h1 class="person-name">Clara Denholm</h1>
      <p class="person-title">CEO/ Founder</p>
      <p class="office-line">12th floor, Corvale<br>Tower Hillmont</p>
      <ul class="contact-list">
        <li>
          <svg viewBox="0 0 24 24"><path d="M6.6 10.8a15.1 15.1 0 0 0 6.6 6.6l2.2-2.2a1 1 0 0 1 1-.25 11.4 11.4 0 0 0 3.6.57 1 1 0 0 1 1 1V20a1 1 0 0 1-1 1A17 17 0 0 1 3 4a1 1 0 0 1 1-1h3.5a1 1 0 0 1 1 1c0 1.25.2 2.45.57 3.57a1 1 0 0 1-.25 1z"/></svg>
          (55) 4210 7780 ext. 214
        </li>
        <li>
          <svg viewBox="0 0 24 24"><path d="M7 1h10a2 2 0 0 1 2 2v18a2 2 0 0 1-2 2H7a2 2 0 0 1-2-2V3a2 2 0 0 1 2-2zm0 3v14h10V4zm5 15.5a1.2 1.2 0 1 0 0 2.4 1.2 1.2 0 0 0 0-2.4z"/></svg>
          56 2207 4168
        </li>
        <li>
          <svg viewBox="0 0 24 24"><path d="M2 5h20v14H2zm2 2v.5l8 5 8-5V7zm0 2.8V17h16V9.8l-8 5z"/></svg>
          clara@brambleware.com.au
        </li>
        <li>
          <svg viewBox="0 0 24 24"><path d="M12 2a10 10 0 1 0 0 20 10 10 0 0 0 0-20zm6.9 9h-3a15 15 0 0 0-1.2-5.4A8 8 0 0 1 18.9 11zM12 4.1c.9 1.2 1.8 3.6 1.9 6.9h-3.8c.1-3.3 1-5.7 1.9-6.9zM9.3 5.6A15 15 0 0 0 8.1 11h-3a8 8 0 0 1 4.2-5.4zM5.1 13h3a15 15 0 0 0 1.2 5.4A8 8 0 0 1 5.1 13zm6.9 6.9c-.9-1.2-1.8-3.6-1.9-6.9h3.8c-.1 3.3-1 5.7-1.9 6.9zm2.7-1.5a15 15 0 0 0 1.2-5.4h3a8 8 0 0 1-4.2 5.4z"/></svg>
          www.brambleware.com.au
        </li>
      </ul>
    </div>

    <div class="brand-lockup">
      <span class="brand-mark" aria-hidden="true"></span>
      <span class="brand-name">BrambleWare</span>
    </div>
  </section>

  <section class="card logo-side" aria-label="Card back with brand">
    <div class="logo-center">
      <span class="brand-mark" aria-hidden="true"></span>
      <div class="brand-text">
        <div class="brand-name">BrambleWare</div>
        <div class="brand-rule"></div>
        <div class="tagline">Student Success Platform</div>
      </div>
    </div>
  </section>

</main>
</body>
</html>
```